A private psychotherapy practice for seniors located on the upper west side of manhattan needs a pos

**Hi, Please note deadline was decreased by two days**

I am a Psychotherapist (LCSW) who has a Private Practice located on the Upper West Side of Manhattan. I accept Vitalcare and most other insurances. I treat Seniors who have health or financial issues, loss of spouse, feel sad most days, withdraw from social activities or have problems sleeping or eating. Psychotherapy allows individuals to relieve their feelings of sadness and to enjoy life again. I am a licensed clinical social worker with over fifteen years of experience and advanced training from Calderwood Analytic Academy.

Target Market(s)

Senior Citizens (65+) living on the upper west side of manhattan

Font styles to use
Serif

Requirements
Must have
• Broad appeal - diversified ethnic group if photos are used. Clear call to help those struggling with aging issues - especially living in New York City
Nice to have
• Hopeful and improved quality of life as result of psychotherapy treatment. Improved relations with family and friends.
Should not have
• Not depressing or too psycho bable.

```html
<!DOCTYPE html>
<html lang="en">
<head>
<meta charset="utf-8">
<title>Senior Psychotherapy Postcard</title>
<link href="https://fonts.googleapis.com/css2?family=Open+Sans:wght@400;600;700;800&family=Roboto+Condensed:wght@700&display=swap" rel="stylesheet">
<style>
:root{
  --backdrop:#8a8d91;
  --navy:#0f2f63;
  --blue:#1d5fb0;
  --sky:#3f8fd6;
  --green:#7cc12b;
  --green-dark:#4f9a1a;
  --white:#ffffff;
  --ink:#1c2a3a;
}
*{margin:0;padding:0;box-sizing:border-box}
html,body{width:791px;height:1200px;overflow:hidden}
body{background:var(--backdrop);font-family:"Open Sans",Arial,sans-serif;position:relative}
.card{position:absolute;left:48px;width:697px;background:var(--white);overflow:hidden;box-shadow:0 6px 18px rgba(0,0,0,.35)}
.card--front{top:32px;height:535px}
.card--back{top:612px;height:548px}

.front__topbar{position:absolute;top:0;left:0;right:0;height:14px;background:linear-gradient(90deg,var(--green) 0 60%,var(--blue) 60%)}
.front__photo{position:absolute;top:22px;left:14px;right:14px;height:350px;background:linear-gradient(180deg,#eef2f6 0%,#d7dfe8 55%,#b8c6d6 100%)}
.front__badge{position:absolute;left:52px;top:120px;width:170px;height:170px}
.front__badge-text{position:absolute;left:52px;top:150px;width:170px;text-align:center;color:var(--navy);font-weight:800;line-height:1.05}
.front__badge-text .big{font-size:30px;display:block}
.front__badge-text .mid{font-size:20px;display:block;color:var(--white)}
.front__badge-text .sm{font-size:15px;display:block}
.front__band{position:absolute;left:0;top:340px;width:697px;height:195px}
.front__headline{position:absolute;left:26px;top:386px;color:var(--white);font-family:"Roboto Condensed",Arial,sans-serif;text-transform:uppercase;line-height:1.12}
.front__headline .l1{font-size:21px;display:block}
.front__headline .l2{font-size:30px;color:var(--green);display:block}
.front__headline .l3{font-size:14px;display:block;font-family:"Open Sans",Arial,sans-serif;font-weight:600}
.contacts{position:absolute;list-style:none;font-size:14px;line-height:20px}
.contacts li{display:flex;align-items:center;gap:8px}
.contacts svg{width:12px;height:12px;flex:none}
.front__contacts{left:26px;top:470px;color:var(--ink)}
.front__panel{position:absolute;left:400px;top:382px;width:297px;height:120px;background:var(--navy);color:var(--white);padding:14px 16px;font-size:15px;line-height:1.3}
.front__panel .hl{color:var(--green)}
.front__panel strong{font-weight:700}
.front__follow{position:absolute;left:400px;top:502px;width:297px;height:33px;background:var(--blue);color:var(--white);display:flex;align-items:center;justify-content:flex-end;gap:10px;padding-right:18px;font-size:15px;font-weight:600}
.front__follow .dot{width:20px;height:20px;border-radius:50%;background:var(--green)}

.back__band{position:absolute;left:0;top:0;width:330px;height:548px}
.back__copy{position:absolute;left:22px;top:30px;width:228px;color:var(--white);font-size:14.5px;line-height:1.3;text-align:justify;hyphens:auto}
.back__photo{position:absolute;left:139px;top:286px;width:156px;height:156px;border-radius:50%;border:6px solid var(--white);background:radial-gradient(circle at 45% 40%,#e6eef7,#9fb7d2 70%,#6f8fb4);box-shadow:0 0 0 4px var(--green)}
.back__contacts{left:22px;top:472px;color:var(--white)}
.back__stamp{position:absolute;left:549px;top:37px;width:101px;height:103px;border:2px solid #7d8590}
</style>
</head>
<body>

<section class="card card--front">
  <div class="front__topbar"></div>
  <div class="front__photo" role="img" aria-label="Photo of a smiling, diverse group of senior men and women standing together"></div>

  <svg class="front__badge" viewBox="0 0 100 100" aria-hidden="true">
    <polygon fill="#7cc12b" points="50,0 58,12 72,5 74,20 89,18 84,33 98,38 88,50 98,62 84,67 89,82 74,80 72,95 58,88 50,100 42,88 28,95 26,80 11,82 16,67 2,62 12,50 2,38 16,33 11,18 26,20 28,5 42,12"/>
  </svg>
  <div class="front__badge-text">
    <span class="big">Accept</span>
    <span class="mid">Vitalcare</span>
    <span class="sm">and other<br>Insurance</span>
  </div>

  <svg class="front__band" viewBox="0 0 697 195" preserveAspectRatio="none" aria-hidden="true">
    <path d="M0 30 Q 200 60 420 42 L697 30 L697 195 L0 195Z" fill="#ffffff"/>
    <path d="M0 30 Q 200 60 420 42 L420 120 Q 200 110 0 128Z" fill="#1d5fb0"/>
    <path d="M0 22 Q 200 52 420 34 L420 44 Q 200 62 0 32Z" fill="#7cc12b"/>
    <path d="M0 128 Q 200 110 420 120 L420 128 Q 200 118 0 136Z" fill="#7cc12b"/>
    <path d="M250 195 Q 330 155 400 162 L400 195Z" fill="#4f9a1a"/>
  </svg>

  <h1 class="front__headline">
    <span class="l1">A Private Psychotherapy Practice</span>
    <span class="l2">For Seniors Located</span>
    <span class="l3">On the Upper West Side of Manhattan</span>
  </h1>

  <ul class="contacts front__contacts">
    <li><svg viewBox="0 0 16 16"><path fill="#4f9a1a" d="M3 1h3l1.5 4-2 1.5a9 9 0 0 0 4 4l1.5-2 4 1.5v3a2 2 0 0 1-2 2A13 13 0 0 1 1 3a2 2 0 0 1 2-2z"/></svg>212-555-0147</li>
    <li><svg viewBox="0 0 16 16"><circle cx="8" cy="8" r="7" fill="#4f9a1a"/></svg>hello@westsidecounsel.com</li>
    <li><svg viewBox="0 0 16 16"><circle cx="8" cy="8" r="7" fill="#4f9a1a"/></svg>westsidecounsel.com</li>
  </ul>

  <div class="front__panel">
    <strong>Licensed clinical social worker</strong><br>
    with over <span class="hl">15 years of experience</span><br>
    and <span class="hl">advanced training</span> from<br>
    Calderwood Analytic Academy
  </div>
  <div class="front__follow">Follow us <span class="dot"></span><span class="dot"></span></div>
</section>

<section class="card card--back">
  <svg class="back__band" viewBox="0 0 330 548" preserveAspectRatio="none" aria-hidden="true">
    <defs>
      <linearGradient id="bandBlue" x1="0" y1="0" x2="1" y2="1">
        <stop offset="0" stop-color="#1d5fb0"/>
        <stop offset="1" stop-color="#0f2f63"/>
      </linearGradient>
    </defs>
    <path d="M0 0 H300 Q 250 270 305 548 H0Z" fill="#7cc12b"/>
    <path d="M0 0 H290 Q 238 270 294 548 H0Z" fill="url(#bandBlue)"/>
  </svg>

  <p class="back__copy" lang="en">I am a Psychotherapist (LCSW) who has a Private Practice located on the Upper West Side of Manhattan I treat Seniors who have health or financial issues, loss of spouse, feel sad most days, withdraw from social activities or have problems sleeping or eating. Psychotherapy allows individuals to relieve their feelings of sadness and to enjoy life again.</p>

  <div class="back__photo" role="img" aria-label="Close-up photo of a stethoscope resting on a laptop keyboard"></div>

  <ul class="contacts back__contacts">
    <li><svg viewBox="0 0 16 16"><path fill="#7cc12b" d="M3 1h3l1.5 4-2 1.5a9 9 0 0 0 4 4l1.5-2 4 1.5v3a2 2 0 0 1-2 2A13 13 0 0 1 1 3a2 2 0 0 1 2-2z"/></svg>212-555-0147</li>
    <li><svg viewBox="0 0 16 16"><circle cx="8" cy="8" r="7" fill="#7cc12b"/></svg>hello@westsidecounsel.com</li>
    <li><svg viewBox="0 0 16 16"><circle cx="8" cy="8" r="7" fill="#7cc12b"/></svg>westsidecounsel.com</li>
  </ul>

  <div class="back__stamp"></div>
</section>

</body>
</html>
```